Brindlow Electrical Solutions needs a website

We need a new website designed because our current one is outdated. I would like a one-page website. We are a B2B company and want to maintain a professional appearance to appeal to project managers and directors.

for some reference, these are a few of my competitor's websites; we offer the same services.

https://valtorwiring.com.au/services
https://www.dunsary.com.au/mechanical-electrical-services/
https://www.gravik.com.au/

Industry/Entity Type

Electrical

Number of Pages Required

1 page

Font styles to use
Sans Serif

Colors
0054AA
0677BA
7BADD7
CADEEF
E8F1F8

```html
<!DOCTYPE html>
<html lang="en">
<head>
<meta charset="utf-8">
<title>Brindlow Electrical Solutions</title>
<link href="https://fonts.googleapis.com/css2?family=Russo+One&family=Montserrat:wght@500;600;700&family=Inter:wght@400;500;600&display=swap" rel="stylesheet">
<style>
:root{
  --blue-deep:#0054AA;
  --blue:#0677BA;
  --blue-mid:#7BADD7;
  --blue-pale:#CADEEF;
  --blue-mist:#E8F1F8;
  --navy:#0b3f78;
  --ink:#1d1d1f;
  --body:#3b4451;
  --rule:#5a6470;
  --footer:#1b1b1d;
  --white:#fff;
}
*{margin:0;padding:0;box-sizing:border-box}
html,body{width:1200px;height:3173px;overflow:hidden;background:var(--white)}
body{position:relative;font-family:"Inter",Arial,sans-serif;color:var(--ink)}
.abs{position:absolute}
.display{font-family:"Russo One",Arial,sans-serif;letter-spacing:2px}

/* header */
.site-header{left:0;top:0;width:1200px;height:94px;background:var(--white);z-index:5;box-shadow:0 1px 4px rgba(0,0,0,.08)}
.brand{left:110px;top:24px;display:flex;align-items:center;gap:12px}
.brand-mark{width:46px;height:46px;border-radius:50%;background:var(--blue-deep)}
.brand-name{font-family:"Montserrat",Arial,sans-serif;font-weight:700;font-size:17px;color:var(--blue);line-height:1.1;width:190px}
.topbar{left:422px;top:0;width:778px;height:40px;background:var(--blue-deep);border-bottom-left-radius:34px;display:flex;align-items:center;gap:44px;padding-left:102px;color:var(--white);font-size:15px}
.topbar span{display:flex;align-items:center;gap:12px}
.topbar b{font-weight:600}
.nav{left:439px;top:58px;display:flex;gap:44px;font-family:"Montserrat",Arial,sans-serif;font-weight:500;font-size:14px;letter-spacing:.8px;color:var(--ink)}
.nav a{color:inherit;text-decoration:none}
.nav .active{color:var(--blue-deep);font-weight:700;border-bottom:2px solid var(--blue-deep);padding-bottom:2px}

/* hero */
.hero{left:0;top:94px;width:1200px;height:600px;overflow:hidden}
.hero-photo{left:0;top:0;width:1200px;height:600px;background:linear-gradient(100deg,#1c2a3c 0%,#2f3d4f 35%,#6a7582 60%,#25508c 85%,#153b6d 100%)}
.hero-text{left:110px;top:104px;color:var(--white)}
.hero-kicker{font-size:26px;margin-left:2px}
.hero-title{font-size:50px;line-height:56px;margin-top:10px;letter-spacing:4px}
.hero-sub{font-family:"Inter",Arial,sans-serif;font-weight:600;font-size:17px;margin-top:16px;margin-left:1px}
.btn{display:inline-block;background:var(--blue-deep);color:var(--white);font-family:"Montserrat",Arial,sans-serif;font-weight:700;font-size:14px;letter-spacing:.5px;padding:16px 14px;margin-top:20px;margin-left:2px}
.hero-curve{left:0;top:0}

/* section titles */
.sec-title{width:1200px;text-align:center;font-size:32px;color:var(--blue-deep)}
.sec-title .accent{color:var(--blue)}
.sec-rule{width:58px;height:4px;background:var(--rule);left:571px}

/* services */
.card{width:308px;height:344px;top:873px;background:var(--white);border-radius:12px;box-shadow:0 2px 10px rgba(0,0,0,.12)}
.card-photo{position:absolute;left:12px;top:12px;width:284px;height:220px;border-radius:10px}
.card-icon{position:absolute;left:122px;top:196px;width:64px;height:64px;border-radius:50%;background:var(--blue);border:4px solid var(--white);display:flex;align-items:center;justify-content:center}
.card-title{position:absolute;left:0;top:268px;width:308px;text-align:center;font-family:"Montserrat",Arial,sans-serif;font-weight:600;font-size:14px;line-height:28px;letter-spacing:.6px}
.round-arrow{width:26px;height:26px;border:1.6px solid var(--ink);border-radius:50%;display:flex;align-items:center;justify-content:center;top:1032px}

/* projects */
.projects{left:0;top:1336px;width:1200px;height:780px;background:linear-gradient(100deg,#0d4f90 0%,#0b5aa0 40%,#1c84c4 100%)}
.proj-photo{left:111px;top:1507px;width:977px;height:521px;border-radius:16px;background:linear-gradient(90deg,#7c6f66 0%,#9a8f86 30%,#a7a29c 55%,#8f8880 80%,#6e6862 100%)}
.proj-card{left:743px;top:1625px;width:282px;height:286px;background:var(--white);padding:26px 25px}
.proj-card h3{font-size:19px;line-height:31px;color:var(--blue-deep);letter-spacing:1.5px}
.proj-card p{font-size:15px;line-height:31px;color:var(--body);margin-top:12px}
.slide-btn{left:81px;width:58px;height:58px;border-radius:50%;background:var(--white);display:flex;align-items:center;justify-content:center}

/* about */
.about-halo{left:140px;top:2210px;width:420px;height:430px;border-radius:50%;background:radial-gradient(circle,var(--blue-pale) 55%,var(--blue-mist) 80%,transparent 81%)}
.about-ring{left:172px;top:2252px;width:356px;height:356px;border-radius:50%;background:var(--white)}
.about-photo{left:184px;top:2264px;width:332px;height:332px;border-radius:50%;background:linear-gradient(120deg,#cfd2d4 0%,#9aa1a7 50%,#44484d 100%)}
.about-copy{left:637px;top:2222px;width:440px}
.about-copy h2{font-size:32px;color:var(--blue-deep)}
.about-copy h2 .accent{color:var(--blue)}
.about-rule{width:58px;height:4px;background:var(--rule);margin-top:10px}
.about-copy h4{font-family:"Montserrat",Arial,sans-serif;font-weight:600;font-size:17px;letter-spacing:1px;color:#4a5866;margin-top:24px}
.about-copy p{font-size:15px;line-height:31px;color:var(--body);margin-top:8px}
.about-copy p+p{margin-top:31px}

/* footer */
.site-footer{left:0;top:2728px;width:1200px;height:445px;background:var(--footer);color:var(--white)}
.f-head{font-size:23px;letter-spacing:1px;top:58px}
.f-links{left:99px;top:107px;list-style:none;font-size:15px;line-height:31px}
.f-links li{display:flex;align-items:center;gap:12px}
.socials{left:98px;top:280px;display:flex;gap:8px}
.socials span{width:31px;height:31px;border:1.3px solid var(--white);border-radius:50%}
.f-divider{top:88px;height:240px;border-left:1px dashed #777}
.contact-item{left:355px;display:flex;gap:14px}
.contact-item .ic{width:33px;height:33px;border-radius:50%;background:var(--blue);display:flex;align-items:center;justify-content:center;flex-shrink:0;margin-top:4px}
.contact-item .lbl{font-size:18px;font-weight:500;line-height:30px}
.contact-item .val{font-size:16px;line-height:32px}
.c-rule{left:355px;width:240px;border-top:1px dashed #888}
.field{left:716px;width:352px;height:40px;border:1px solid #cfd3d8;border-radius:2px;font-size:14px;padding:11px 12px;color:#e5e5e5}
.submit{left:716px;top:2989px;width:352px;height:38px;background:linear-gradient(90deg,var(--blue-deep),var(--blue));text-align:center;font-family:"Russo One",Arial,sans-serif;font-size:15px;line-height:38px;letter-spacing:1px}
.f-bottom-rule{left:99px;top:3116px;width:1002px;border-top:1px solid #9aa0a6}
.copyright{left:0;top:3139px;width:1200px;text-align:center;font-size:15px}
</style>
</head>
<body>

<header class="abs site-header">
  <div class="abs brand"><span class="brand-mark"></span><span class="brand-name">Brindlow Electrical Solutions</span></div>
  <div class="abs topbar">
    <span><svg width="26" height="26" viewBox="0 0 26 26"><circle cx="13" cy="13" r="13" fill="#fff"/><path d="M9 7.5l2.4 2.6-1.2 1.6c.8 1.8 2.2 3.2 4 4l1.6-1.2 2.6 2.4-1.4 2c-4.6-.4-8.6-4.4-9-9z" fill="#0054AA"/></svg><b>Phone:</b> 02 7450 3921</span>
    <span><svg width="26" height="26" viewBox="0 0 26 26"><circle cx="13" cy="13" r="13" fill="#fff"/><rect x="7" y="8.5" width="12" height="9" rx="1" fill="#0054AA"/><path d="M7.5 9.5l5.5 4 5.5-4" stroke="#fff" stroke-width="1.2" fill="none"/></svg><b>Email:</b> info@brindlowelectrical.com.au</span>
  </div>
  <nav class="abs nav"><a class="active">HOME</a><a>ABOUT</a><a>LATEST PROJECTS</a><a>SERVICES</a><a>CONTACT US</a></nav>
</header>

<section class="abs hero">
  <div class="abs hero-photo" role="img" aria-label="Technician testing a switchboard with a clamp meter"></div>
  <div class="abs hero-text display">
    <div class="hero-kicker">WELCOME TO</div>
    <h1 class="hero-title">BRINDLOW<br>ELECTRICAL<br>SOLUTIONS</h1>
    <div class="hero-sub">MECHANICAL ELECTRICAL HVAC</div>
    <span class="btn">GET STARTED</span>
  </div>
  <svg class="abs hero-curve" width="1200" height="600" viewBox="0 0 1200 600">
    <path d="M0 506 C240 580 500 600 760 578 C960 560 1100 525 1200 498 L1200 600 L0 600Z" fill="#fff"/>
    <path d="M240 562 C520 610 880 590 1200 510 L1200 528 C880 606 520 612 240 562Z" fill="#0677BA"/>
  </svg>
</section>

<h2 class="abs sec-title display" style="top:780px">OUR <span class="accent">SERVICES</span></h2>
<div class="abs sec-rule" style="top:830px"></div>

<div class="abs round-arrow" style="left:42px"><svg width="10" height="10" viewBox="0 0 10 10"><path d="M6.5 1.5L3 5l3.5 3.5" stroke="#1d1d1f" stroke-width="1.6" fill="none"/></svg></div>
<div class="abs round-arrow" style="left:1124px"><svg width="10" height="10" viewBox="0 0 10 10"><path d="M3.5 1.5L7 5 3.5 8.5" stroke="#1d1d1f" stroke-width="1.6" fill="none"/></svg></div>

<article class="abs card" style="left:110px">
  <div class="card-photo" role="img" aria-label="Electrician sorting coloured wiring" style="background:linear-gradient(135deg,#16314f,#2f5f8e 50%,#b08a3a)"></div>
  <div class="card-icon"><svg width="28" height="28" viewBox="0 0 28 28" fill="none" stroke="#fff" stroke-width="1.8"><rect x="3" y="3" width="10" height="8"/><circle cx="19" cy="19" r="5"/><path d="M3 17h8M3 22h8"/></svg></div>
  <h3 class="card-title">MECHANICAL ELECTRICAL<br>SERVICES</h3>
</article>
<article class="abs card" style="left:444px">
  <div class="card-photo" role="img" aria-label="Electrician in hard hat working on a distribution board" style="background:linear-gradient(120deg,#4d5459,#8e9398 50%,#5e5246)"></div>
  <div class="card-icon"><svg width="28" height="28" viewBox="0 0 28 28" fill="none" stroke="#fff" stroke-width="1.8"><rect x="4" y="3" width="20" height="22" rx="1"/><rect x="8" y="7" width="5" height="5"/><rect x="15" y="7" width="5" height="5"/><rect x="8" y="15" width="5" height="5"/><rect x="15" y="15" width="5" height="5"/></svg></div>
  <h3 class="card-title">SWITCHBOARD DESIGN &amp;<br>INSTALLATION</h3>
</article>
<article class="abs card" style="left:778px">
  <div class="card-photo" role="img" aria-label="High-rise buildings under construction with tower cranes" style="background:linear-gradient(180deg,#6e9cc9,#a9c4dd 45%,#6f7a6e)"></div>
  <div class="card-icon"><svg width="28" height="28" viewBox="0 0 28 28" fill="none" stroke="#fff" stroke-width="1.8"><rect x="5" y="6" width="9" height="19"/><rect x="14" y="11" width="9" height="14"/><path d="M8 10h3M8 14h3M8 18h3M17 15h3M17 19h3"/></svg></div>
  <h3 class="card-title">COMMERCIAL &amp; INDUSTRIAL<br>PROJECTS</h3>
</article>

<section class="abs projects"></section>
<h2 class="abs sec-title display" style="top:1418px;color:#fff">LATEST PROJECTS</h2>
<div class="abs sec-rule" style="top:1472px;background:#fff"></div>
<div class="abs proj-photo" role="img" aria-label="Plant room with switchboards and cable trays against a block wall"></div>
<div class="abs proj-card">
  <h3 class="display">MECHANICAL<br>ELECTRICAL<br>SERVICES</h3>
  <p>Excepteur sint occaecat cupidatat non proident, sunt in culpa qui officia deserunt mollit anim id est laborum.</p>
</div>
<div class="abs slide-btn" style="top:1697px"><svg width="14" height="22" viewBox="0 0 14 22"><path d="M3 2l9 9-9 9" stroke="#555" stroke-width="2" fill="none"/></svg></div>
<div class="abs slide-btn" style="top:1781px"><svg width="14" height="22" viewBox="0 0 14 22"><path d="M11 2L2 11l9 9" stroke="#555" stroke-width="2" fill="none"/></svg></div>

<div class="abs about-halo"></div>
<div class="abs about-ring"></div>
<div class="abs about-photo" role="img" aria-label="Technician servicing an air conditioning unit"></div>
<div class="abs about-copy">
  <h2 class="display">ABOUT <span class="accent">US</span></h2>
  <div class="about-rule"></div>
  <h4>BRINDLOW ELECTRICAL SOLUTIONS</h4>
  <p>Lorem ipsum dolor sit amet, consectetur adipiscing elit, sed do eiusmod tempor incididunt ut labore et dolore magna aliqua. Ut enim ad minim veniam, quis nostrud exercitation ullamco laboris nisi ut aliquip ex ea commodo consequat.</p>
  <p>Duis aute irure dolor in reprehenderit in voluptate velit esse cillum dolore eu fugiat nulla pariatur. Excepteur sint occaecat cupidatat non proident, sunt in culpa qui officia deserunt mollit anim id est laborum.</p>
</div>

<footer class="abs site-footer">
  <h3 class="abs f-head display" style="left:98px">Quick Links</h3>
  <ul class="abs f-links">
    <li><svg width="14" height="12" viewBox="0 0 14 12"><path d="M1 6h11M7 1l5 5-5 5" stroke="#fff" stroke-width="2" fill="none"/></svg>Home</li>
    <li><svg width="14" height="12" viewBox="0 0 14 12"><path d="M1 6h11M7 1l5 5-5 5" stroke="#fff" stroke-width="2" fill="none"/></svg>About</li>
    <li><svg width="14" height="12" viewBox="0 0 14 12"><path d="M1 6h11M7 1l5 5-5 5" stroke="#fff" stroke-width="2" fill="none"/></svg>Latest Projects</li>
    <li><svg width="14" height="12" viewBox="0 0 14 12"><path d="M1 6h11M7 1l5 5-5 5" stroke="#fff" stroke-width="2" fill="none"/></svg>Services</li>
    <li><svg width="14" height="12" viewBox="0 0 14 12"><path d="M1 6h11M7 1l5 5-5 5" stroke="#fff" stroke-width="2" fill="none"/></svg>Contact&nbsp; us</li>
  </ul>
  <div class="abs socials"><span></span><span></span><span></span></div>
  <div class="abs f-divider" style="left:301px"></div>

  <h3 class="abs f-head display" style="left:355px">Contact Details</h3>
  <div class="abs contact-item" style="top:104px">
    <span class="ic"><svg width="16" height="16" viewBox="0 0 16 16"><path d="M3 2l2.6 2.8-1.3 1.7c.9 1.9 2.3 3.3 4.2 4.2l1.7-1.3L13 12l-1.5 2C6.6 13.6 2.4 9.4 2 4.5z" fill="#fff"/></svg></span>
    <div><div class="lbl">Phone;</div><div class="val">02 7450 3921</div></div>
  </div>
  <div class="abs c-rule" style="top:166px"></div>
  <div class="abs contact-item" style="top:186px">
    <span class="ic"><svg width="16" height="16" viewBox="0 0 16 16"><rect x="2" y="3.5" width="12" height="9" rx="1" fill="#fff"/><path d="M2.5 4.5L8 8.5l5.5-4" stroke="#0677BA" stroke-width="1.2" fill="none"/></svg></span>
    <div><div class="lbl">Email:</div><div class="val">info@brindlowelectrical.com.au</div></div>
  </div>
  <div class="abs c-rule" style="top:248px"></div>
  <div class="abs contact-item" style="top:278px">
    <span class="ic"><svg width="16" height="16" viewBox="0 0 16 16"><path d="M8 1.5a4.5 4.5 0 0 0-4.5 4.5c0 3.4 4.5 8.5 4.5 8.5s4.5-5.1 4.5-8.5A4.5 4.5 0 0 0 8 1.5z" fill="#fff"/><circle cx="8" cy="6" r="1.6" fill="#0677BA"/></svg></span>
    <div><div class="lbl">Address:</div><div class="val">Sydney NSW, Australia</div></div>
  </div>
  <div class="abs f-divider" style="left:670px"></div>

  <h3 class="abs f-head display" style="left:716px">Contact Me</h3>
</footer>
<div class="abs field" style="top:2829px">Name:</div>
<div class="abs field" style="top:2882px">Email:</div>
<div class="abs field" style="top:2934px">Address:</div>
<div class="abs submit" style="color:#fff">Submit Now</div>
<div class="abs f-bottom-rule"></div>
<div class="abs copyright" style="color:#fff">Copyrights@2024.Company Name.All Rights Reserved</div>

</body>
</html>
```